Business Card Design - Law Firm

We are a boutique law firm located near the beach in Manly, Australia. We have recently had a new logo designed and are revamping our business cards with the new logo.

We have recently had a business card design done for us but are not entirely happy with it. We are looking for something modern, simplistic but striking. We would like to see multiple designs.

We have attached a word document which includes our new logo and the current business card design which we are looking at moving away from.

We would like the business cards to be double sided. We would like the design to include something which we can print in gloss colour when we send it to the business card printers.

```html
<!DOCTYPE html>
<html lang="en">
<head>
<meta charset="utf-8">
<title>Hartwell &amp; Associates – Business Card</title>
<link rel="stylesheet" href="https://fonts.googleapis.com/css2?family=Jura:wght@400;500;600&display=swap">
<style>
  :root {
    --backdrop: #1d1d22;
    --card-light: #f4f4f2;
    --card-dark: #2f2f31;
    --accent-orange: #e5673c;
    --text-grey: #4a4a4e;
    --brand-violet: #5b50b4;
  }
  * { box-sizing: border-box; margin: 0; padding: 0; }
  html, body {
    width: 1200px; height: 800px; overflow: hidden;
    background: var(--backdrop);
    font-family: "Jura", sans-serif;
  }
  .canvas { position: relative; width: 1200px; height: 800px; }
  .card {
    position: absolute;
    width: 540px; height: 330px;
    border-radius: 3px;
    box-shadow: 0 18px 40px rgba(0,0,0,.45);
  }
  .card-front { left: 50px; top: 140px; background: var(--card-light); }
  .card-back  { left: 610px; top: 330px; background: var(--card-dark); }

  .front-brand {
    position: absolute; top: 26px; right: 28px;
    display: flex; align-items: center; gap: 8px;
    color: var(--brand-violet); font-weight: 600; font-size: 13px;
    letter-spacing: .5px;
  }
  .brand-dot { width: 14px; height: 14px; border-radius: 50%; background: var(--brand-violet); }

  .person { position: absolute; left: 34px; top: 118px; }
  .person-name {
    color: var(--accent-orange); font-size: 34px; font-weight: 500;
    letter-spacing: 2px; word-spacing: 14px;
  }
  .person-role {
    color: var(--text-grey); font-size: 16px; letter-spacing: 1.5px;
    word-spacing: 10px; margin-left: 70px; margin-top: 2px;
  }

  .contact {
    position: absolute; right: 30px; bottom: 34px;
    display: grid; grid-template-columns: auto auto;
    column-gap: 16px; row-gap: 4px; align-items: baseline;
  }
  .contact-label { color: var(--accent-orange); font-size: 15px; font-weight: 500; letter-spacing: 1px; }
  .contact-value { color: var(--text-grey); font-size: 11px; letter-spacing: .5px; }
  .contact-value.address { text-transform: uppercase; line-height: 1.3; }

  .back-brand {
    position: absolute; inset: 0;
    display: flex; align-items: center; justify-content: center; gap: 14px;
  }
  .back-brand .brand-dot { width: 30px; height: 30px; }
  .back-brand-name {
    color: var(--brand-violet); font-size: 24px; font-weight: 500; letter-spacing: 1.5px;
  }
</style>
</head>
<body>
<main class="canvas">
  <section class="card card-front">
    <div class="front-brand">
      <span class="brand-dot"></span>
      <span>Hartwell &amp; Associates</span>
    </div>
    <div class="person">
      <p class="person-name">Maren Ellison</p>
      <p class="person-role">practice manager</p>
    </div>
    <div class="contact">
      <span class="contact-label">Contact</span>
      <span class="contact-value">(02) 5550 1847</span>
      <span class="contact-label">Email</span>
      <span class="contact-value">maren.ellison@harbourlaw.com.au</span>
      <span class="contact-label">Website</span>
      <span class="contact-value">www.hartwellassociates.com.au</span>
      <span class="contact-label">Place</span>
      <span class="contact-value address">Suite 4, 18 Ocean Walk<br>Shelly Bay NSW 2099</span>
    </div>
  </section>

  <section class="card card-back">
    <div class="back-brand">
      <span class="brand-dot"></span>
      <span class="back-brand-name">Hartwell &amp; Associates Lawyers</span>
    </div>
  </section>
</main>
</body>
</html>
```